Brackenford Solar Project Sign - 36" x 48" color poster

Need a 36" x 48" sign to put next to our solar project. The solar project is installed and we will print this sign on plastic corrugated board and mount as an informational kiosk next to the project. A picture of a similar kiosk is attached. Its is important that the information is easy to understand and aesthetically pleasing. I've uploaded a draft that we did with the information and general idea. The draft is not the correct dimensions and will not scale to the appropriate size. Looking for a professional to do this well. Thank you !!
Target Market(s)
teenage school children and their parents.
Industry/Entity Type
Solar Energy
Requirements
Must have
- technical information included in the draft. Must include the photo of the solar project. Must include the Tallow Brook Solar Logo. Must be scaled to 36" x 48".
Nice to have
- Color scheme that complements the tallow brook solar logo colors
Should not have
- stock photos

```html
<!DOCTYPE html>
<html lang="en">
<head>
<meta charset="utf-8">
<title>Brackenford School District Solar</title>
<link href="https://fonts.googleapis.com/css2?family=Montserrat:wght@600;800&family=Roboto+Slab:wght@400;700&display=swap" rel="stylesheet">
<style>
  :root {
    --bg: #eeeff1;
    --navy: #0f2a44;
    --navy-deep: #081a2e;
    --teal: #12a6b5;
    --green: #6aab45;
    --orange: #f7941d;
    --white: #ffffff;
    --ink: #4a4a4a;
    --grid: #d6d7d9;
    --bar: #4472c4;
    --line: #f5c02a;
    --sky-top: #1d5fc0;
    --sky-low: #8fb5e0;
    --field: #6e5a3e;
  }
  * { box-sizing: border-box; margin: 0; padding: 0; }
  html, body { width: 1200px; height: 900px; overflow: hidden; background: var(--bg); }
  .poster {
    position: relative;
    width: 1200px;
    height: 900px;
    overflow: hidden;
    background: linear-gradient(135deg, #f4f5f6 0%, var(--bg) 60%, #e4e6e8 100%);
    font-family: "Roboto Slab", Georgia, serif;
  }
  .backdrop { position: absolute; inset: 0; }

  .title {
    position: absolute;
    left: 110px;
    top: 64px;
    width: 300px;
    text-align: center;
    font-family: "Montserrat", Arial, sans-serif;
    font-weight: 800;
    color: var(--orange);
    line-height: 1.1;
  }
  .title__line { display: block; font-size: 27px; letter-spacing: 0.5px; }
  .title__line--wide { font-size: 43px; letter-spacing: 14px; margin: 2px 0 4px; padding-left: 14px; }

  .intro {
    position: absolute;
    left: 122px;
    top: 206px;
    width: 276px;
    text-align: center;
    color: var(--white);
    font-weight: 700;
    font-size: 18px;
    line-height: 1.36;
  }

  .panel-diagram {
    position: absolute;
    left: 790px;
    top: 58px;
    width: 240px;
    height: 215px;
    background: linear-gradient(160deg, #c9ced6 0%, #8c97c9 40%, #3f4fb8 55%, #cfd3da 80%);
    clip-path: polygon(2% 3%, 100% 10%, 88% 100%, 0% 82%);
  }
  .panel-labels {
    position: absolute;
    left: 1030px;
    top: 74px;
    list-style: none;
    font-family: "Montserrat", Arial, sans-serif;
    font-weight: 600;
    font-size: 11px;
    color: #555;
  }
  .panel-labels li { height: 26.5px; display: flex; align-items: center; }
  .panel-labels li::before {
    content: "";
    display: inline-block;
    width: 20px;
    height: 1px;
    background: #777;
    margin-right: 9px;
  }

  .benefits {
    position: absolute;
    left: 853px;
    top: 297px;
    width: 292px;
    list-style: none;
    color: var(--orange);
    font-weight: 700;
    font-size: 20px;
    line-height: 1.32;
  }
  .benefits li { position: relative; padding-left: 13px; }
  .benefits li::before { content: "•"; position: absolute; left: 0; }

  .chart { position: absolute; left: 740px; top: 570px; width: 460px; height: 250px; }
  .chart text { font-family: "Montserrat", Arial, sans-serif; }

  .completed {
    position: absolute;
    left: 840px;
    top: 845px;
    display: flex;
    align-items: center;
    gap: 6px;
    font-family: "Montserrat", Arial, sans-serif;
    font-weight: 600;
    font-size: 11px;
    color: var(--green);
  }

  .district-seal {
    position: absolute;
    left: 55px;
    top: 806px;
    width: 50px;
    height: 50px;
    border-radius: 50%;
    border: 3px solid #1c8fd0;
    background: #0f3f73;
  }
  .brand {
    position: absolute;
    left: 135px;
    top: 813px;
    font-family: "Roboto Slab", Georgia, serif;
    font-weight: 700;
    font-size: 28px;
    color: var(--white);
    line-height: 1.2;
  }
</style>
</head>
<body>
<main class="poster">

  <svg class="backdrop" width="1200" height="900" viewBox="0 0 1200 900">
    <defs>
      <linearGradient id="navyFade" x1="0" y1="0" x2="1" y2="1">
        <stop offset="0" stop-color="#18426a"/>
        <stop offset="1" stop-color="#081a2e"/>
      </linearGradient>
      <linearGradient id="tealFade" x1="0" y1="0" x2="0" y2="1">
        <stop offset="0" stop-color="#1bb6c4"/>
        <stop offset="1" stop-color="#0b8697"/>
      </linearGradient>
      <linearGradient id="photoTones" x1="0" y1="0" x2="0" y2="1">
        <stop offset="0" stop-color="#1d5fc0"/>
        <stop offset="0.38" stop-color="#8fb5e0"/>
        <stop offset="0.5" stop-color="#3b3f3a"/>
        <stop offset="0.62" stop-color="#2c4a8a"/>
        <stop offset="0.72" stop-color="#6e5a3e"/>
        <stop offset="1" stop-color="#5a4a35"/>
      </linearGradient>
      <clipPath id="photoCircle"><circle cx="120" cy="190" r="470"/></clipPath>
    </defs>

    <path class="shape-navy" d="M0 560 L640 560 L610 900 L0 900 Z" fill="url(#navyFade)"/>
    <path class="shape-teal" d="M560 330 L775 285 Q770 620 600 900 L420 900 Z" fill="url(#tealFade)"/>
    <circle class="ring-green" cx="150" cy="210" r="522" fill="#6aab45"/>
    <rect class="project-photo" x="0" y="0" width="600" height="670" clip-path="url(#photoCircle)" fill="url(#photoTones)"
          role="img" aria-label="Photo of the school district ground-mounted solar array in a grassy field under a blue sky with clouds"/>
  </svg>

  <h1 class="title">
    <span class="title__line">BRACKENFORD</span>
    <span class="title__line title__line--wide">SCHOOL</span>
    <span class="title__line">DISTRICT SOLAR</span>
  </h1>

  <p class="intro">Incentives from Vermont’s net metering program, renewable energy credits and energy savings pay for this project without adding cost to the district or tax payers</p>

  <div class="panel-diagram" role="img" aria-label="Exploded diagram of solar panel layers"></div>
  <ul class="panel-labels">
    <li>Frame</li>
    <li>Glass</li>
    <li>Encapsulant</li>
    <li>Solar Cells</li>
    <li>Encapsulant</li>
    <li>Backsheet</li>
    <li>Junction Box</li>
  </ul>

  <ul class="benefits">
    <li>Project provides energy savings to school district</li>
    <li>New powerline provides electricity to snack shack</li>
    <li>Provides curriculum opportunity for students</li>
    <li>Solar energy generated without burning fossil</li>
  </ul>

  <svg class="chart" viewBox="740 570 460 250" role="img" aria-label="Monthly expected energy and global horizontal irradiance">
    <g stroke="var(--grid)" stroke-width="1">
      <line x1="818" y1="583" x2="1085" y2="583"/>
      <line x1="818" y1="598.2" x2="1085" y2="598.2"/>
      <line x1="818" y1="613.4" x2="1085" y2="613.4"/>
      <line x1="818" y1="628.6" x2="1085" y2="628.6"/>
      <line x1="818" y1="643.8" x2="1085" y2="643.8"/>
      <line x1="818" y1="659" x2="1085" y2="659"/>
      <line x1="818" y1="674.2" x2="1085" y2="674.2"/>
      <line x1="818" y1="689.4" x2="1085" y2="689.4"/>
      <line x1="818" y1="704.6" x2="1085" y2="704.6"/>
      <line x1="818" y1="719.8" x2="1085" y2="719.8"/>
      <line x1="818" y1="735" x2="1085" y2="735"/>
    </g>
    <g font-size="10" fill="var(--ink)" text-anchor="end">
      <text x="812" y="586">200</text><text x="812" y="601">180</text><text x="812" y="616">160</text>
      <text x="812" y="632">140</text><text x="812" y="647">120</text><text x="812" y="662">100</text>
      <text x="812" y="677">80</text><text x="812" y="692">60</text><text x="812" y="708">40</text>
      <text x="812" y="723">20</text><text x="812" y="738">0</text>
    </g>
    <g font-size="10" fill="var(--ink)">
      <text x="1093" y="586">35000</text><text x="1093" y="608">30000</text><text x="1093" y="629">25000</text>
      <text x="1093" y="651">20000</text><text x="1093" y="673">15000</text><text x="1093" y="694">10000</text>
      <text x="1093" y="716">5000</text><text x="1093" y="738">0</text>
    </g>
    <g fill="var(--bar)">
      <rect x="825.5" y="671.9" width="7" height="63.1"/>
      <rect x="847.7" y="662" width="7" height="73"/>
      <rect x="869.9" y="655.2" width="7" height="79.8"/>
      <rect x="892.1" y="645.3" width="7" height="89.7"/>
      <rect x="914.3" y="624" width="7" height="111"/>
      <rect x="936.5" y="633.2" width="7" height="101.8"/>
      <rect x="958.7" y="613.4" width="7" height="121.6"/>
      <rect x="980.9" y="599.7" width="7" height="135.3"/>
      <rect x="1003.1" y="638.5" width="7" height="96.5"/>
      <rect x="1025.3" y="667.4" width="7" height="67.6"/>
      <rect x="1047.5" y="683.3" width="7" height="51.7"/>
      <rect x="1069.7" y="697" width="7" height="38"/>
    </g>
    <polyline fill="none" stroke="var(--line)" stroke-width="1.8" stroke-linejoin="round"
      points="829,689.4 851.2,678 873.4,660.5 895.6,643.8 917.8,618.7 940,624.8 962.2,604.3 984.4,602 1006.6,647.6 1028.8,678 1051,694.7 1073.2,700.8"/>
    <g font-size="10" fill="var(--ink)" text-anchor="end">
      <text transform="translate(832 744) rotate(-45)">January</text>
      <text transform="translate(854 744) rotate(-45)">February</text>
      <text transform="translate(876 744) rotate(-45)">March</text>
      <text transform="translate(898 744) rotate(-45)">April</text>
      <text transform="translate(920 744) rotate(-45)">May</text>
      <text transform="translate(943 744) rotate(-45)">June</text>
      <text transform="translate(965 744) rotate(-45)">July</text>
      <text transform="translate(987 744) rotate(-45)">August</text>
      <text transform="translate(1009 744) rotate(-45)">September</text>
      <text transform="translate(1031 744) rotate(-45)">October</text>
      <text transform="translate(1054 744) rotate(-45)">November</text>
      <text transform="translate(1076 744) rotate(-45)">December</text>
    </g>
    <g font-size="10" font-weight="600" fill="var(--green)" text-anchor="middle">
      <text transform="translate(764 660) rotate(-90)">Global Horizontal Irradiance</text>
      <text transform="translate(777 660) rotate(-90)">(kWh/m²)</text>
      <text transform="translate(1152 660) rotate(-90)">Expected Energy (kWh)</text>
    </g>
    <rect x="806" y="799" width="30" height="7" fill="var(--bar)"/>
    <text x="840" y="806" font-size="9" fill="#333">Expected Energy</text>
    <line x1="933" y1="802.5" x2="963" y2="802.5" stroke="var(--line)" stroke-width="2"/>
    <text x="968" y="806" font-size="9" fill="#333">Global Horizontal Irradiance</text>
  </svg>

  <p class="completed">
    <svg width="18" height="18" viewBox="0 0 18 18" aria-hidden="true">
      <circle cx="9" cy="9" r="9" fill="var(--orange)"/>
      <path d="M4.5 9.2 L7.6 12.2 L13.5 6" fill="none" stroke="#fff" stroke-width="2" stroke-linecap="round" stroke-linejoin="round"/>
    </svg>
    Project Completed December 2015
  </p>

  <div class="district-seal" role="img" aria-label="School district seal"></div>
  <p class="brand">Tallow Brook Solar</p>

</main>
</body>
</html>
```